Yacht, Boats, Watersports company needs a redesign of business card

Hello Designers!
We are a Boat dealership company that sells fun in the water, we sell boats, Yachts, Kayaks and also yacht WaterSport toys. We are looking to redesign our business cards in to something a little bit more sophisticated. in a way that we can make better use of our company colors. I'm attaching a zipped file containing the company 3 sets of company logo which one is an horizontal another one is a vertical and also a chromed 3d logo. Also is included two set of business cards that we use and also some designs that i think it's interesting. We use PMS 2026c Orange and PMS 7687C Blue. I would like to see at least two different options with the orange as accent and also using blue as an accent color. It's really important for the business cards to have a font option and size that is legible to most people. Our current website is wwww.corvellamarine.com. Please visit if you want to have a better feeling of the Boat dealership
You can send Single sided or double side options. We are now using single sided but we may be open for a double side option if we really like the design.
Target Market(s)
Marine, boat sales, yacht sales, water toys sales/
Contact Information for Business Card
Name: Dale Pritchett
Address: 718 West Halden Lane,
Dania Beach, FL 33019
Phone: 954-382-7146
Fax: 954:382-7139
Cell: 954-451-8320
Email: 212@corvellamarine.com
Website: corvellamarine.com
Requirements
Must have
- the current information of the business card provided.
logo
use the PMS Colors
Nice to have
- a touch of elegance and sophistication but simple
Should not have
- should not have any typography that is hard to read, the card should be simple but yet sophisticated.

```html
<!DOCTYPE html>
<html lang="en">
<head>
<meta charset="utf-8">
<title>Corvella Marine – Business Card</title>
<link href="https://fonts.googleapis.com/css2?family=Michroma&family=Roboto:wght@400&display=swap" rel="stylesheet">
<style>
  :root {
    --backdrop: #2b2b2c;
    --card: #1c1d1f;
    --card-edge: #232427;
    --orange: #f26a2e;
    --blue: #1f4e8c;
    --text: #f2f2f2;
    --rule: #55575b;
    --pattern: #26272a;
  }
  html, body {
    margin: 0;
    padding: 0;
    width: 1200px;
    height: 1108px;
    overflow: hidden;
    background: var(--backdrop);
  }
  .canvas {
    position: relative;
    width: 1200px;
    height: 1108px;
  }
  .card {
    position: absolute;
    top: 190px;
    width: 400px;
    height: 700px;
    background: var(--card);
    border-radius: 22px;
    box-shadow: 0 18px 40px rgba(0,0,0,0.45);
    overflow: hidden;
  }
  .card--front { left: 150px; }
  .card--back { left: 650px; }

  .brand {
    position: absolute;
    top: 120px;
    left: 0;
    right: 0;
    display: flex;
    flex-direction: column;
    align-items: center;
    gap: 18px;
  }
  .brand__dot {
    width: 46px;
    height: 46px;
    border-radius: 50%;
    border: 6px solid var(--orange);
    box-sizing: border-box;
  }
  .brand__name {
    font-family: "Michroma", sans-serif;
    font-size: 20px;
    letter-spacing: 1px;
    color: var(--orange);
    text-transform: uppercase;
    margin: 0;
  }

  .person {
    position: absolute;
    top: 318px;
    left: 0;
    right: 0;
    text-align: center;
    font-family: "Michroma", sans-serif;
    font-size: 21px;
    text-transform: uppercase;
    margin: 0;
  }
  .person__first { color: var(--blue); }
  .person__last { color: var(--orange); }

  .rule {
    width: 140px;
    height: 1px;
    background: var(--rule);
    margin: 0 auto;
  }
  .contact {
    position: absolute;
    top: 372px;
    left: 0;
    right: 0;
    text-align: center;
    font-family: "Roboto", sans-serif;
    color: var(--text);
    font-size: 16px;
    line-height: 22px;
  }
  .contact__list {
    list-style: none;
    margin: 14px 0 14px;
    padding: 0;
  }
  .contact__label { color: var(--orange); }
  .contact__domain { color: var(--orange); }
  .address {
    font-style: normal;
    margin-top: 14px;
    font-size: 17px;
    line-height: 23px;
  }

  .back__pattern {
    position: absolute;
    inset: 0 0 160px 0;
    background: linear-gradient(180deg, var(--pattern), var(--card));
  }
  .back__brand {
    position: absolute;
    right: 40px;
    bottom: 150px;
    display: flex;
    align-items: center;
    gap: 12px;
  }
  .back__brand .brand__name { font-size: 15px; }
  .back__brand .brand__dot { width: 34px; height: 34px; border-width: 5px; }
</style>
</head>
<body>
<main class="canvas">
  <section class="card card--front">
    <header class="brand">
      <span class="brand__dot"></span>
      <p class="brand__name">Corvella Marine</p>
    </header>

    <h1 class="person"><span class="person__first">Dale</span> <span class="person__last">Pritchett</span></h1>

    <div class="contact">
      <div class="rule"></div>
      <ul class="contact__list">
        <li><span class="contact__label">P:</span> 954-382-7146</li>
        <li><span class="contact__label">F:</span> 954:382-7139</li>
        <li><span class="contact__label">M:</span> 954-451-8320</li>
        <li><span class="contact__label">P:</span> 212@corvellamarine.com</li>
        <li>www.<span class="contact__domain">corvellamarine</span>.com</li>
      </ul>
      <div class="rule"></div>
      <address class="address">718 West Halden Lane<br>Dania Beach, FL 33019</address>
    </div>
  </section>

  <section class="card card--back">
    <div class="back__pattern" role="img" aria-label="Faint repeating brand-mark pattern"></div>
    <div class="back__brand">
      <span class="brand__dot"></span>
      <p class="brand__name">Corvella Marine</p>
    </div>
  </section>
</main>
</body>
</html>
```